Prescription Savings Card

Looking to revamp our cards that are distributed to pharmacies. Processing information must stand out and be in black with lines through zeros for easy identification.
I have included some previous card designs for consideration. we are looking to go with something cleaner with mainly processing information on the back similar to all white version attached.
Target Market(s)
Pharmacists and Pharmacy Technicians
Industry/Entity Type
prescription medications
Contact Information for Business Card
processing information
Requirements
Must have
- easy to read processing information

```html
<!DOCTYPE html>
<html lang="en">
<head>
<meta charset="utf-8">
<title>ScriptWay Prescription Savings Card</title>
<link rel="stylesheet" href="https://fonts.googleapis.com/css2?family=Roboto:wght@400;700;900&family=Roboto+Mono:wght@400&display=swap">
<style>
  :root {
    --brand-blue: #2e2785;
    --brand-red: #e3141e;
    --ink: #1b1b1b;
    --card-white: #ffffff;
    --card-black: #0a0a0a;
    --stage: #8a7458;
  }
  * { margin: 0; padding: 0; box-sizing: border-box; }
  html, body { width: 900px; height: 1200px; overflow: hidden; }
  body { background: var(--stage); font-family: "Roboto", Arial, sans-serif; position: relative; }

  .card {
    position: absolute; left: 80px; width: 742px; height: 440px;
    border-radius: 30px; overflow: hidden;
    box-shadow: 0 4px 10px rgba(0,0,0,0.45);
  }
  .card--front { top: 132px; background: var(--card-white); }
  .card--back { top: 640px; background: var(--card-black); }

  .wordmark {
    position: absolute; font-family: "Roboto", Arial, sans-serif;
    font-weight: 900; color: var(--brand-blue); letter-spacing: -3px; line-height: 1;
  }
  .card--front .wordmark { left: 32px; top: 26px; font-size: 92px; }
  .card--back .wordmark { left: 0; right: 0; top: 120px; text-align: center; font-size: 124px; }

  .benefits { position: absolute; left: 30px; top: 150px; list-style: none; }
  .benefits li {
    font-size: 19px; color: var(--ink); height: 24.5px; line-height: 24px;
    padding-left: 18px; position: relative;
  }
  .benefits li::before {
    content: ""; position: absolute; left: 2px; top: 9px; width: 5px; height: 5px;
    border-right: 2px solid var(--brand-red); border-top: 2px solid var(--brand-red);
    transform: rotate(45deg);
  }

  .processing {
    position: absolute; left: 492px; top: 100px; height: 136px;
    border-left: 1.5px solid var(--brand-red); padding-left: 23px;
  }
  .processing .row { display: flex; height: 31px; align-items: center; }
  .processing dt { width: 120px; color: var(--brand-red); font-size: 15px; }
  .processing dd {
    font-family: "Roboto Mono", "Courier New", monospace; font-size: 15px; color: #000;
    font-variant-numeric: slashed-zero;
  }

  .pharmacy-rule { position: absolute; left: 24px; right: 22px; top: 270px; height: 28px; }
  .pharmacy-rule .line-left { position: absolute; left: 0; width: 232px; top: 13px; height: 2px; background: var(--brand-blue); }
  .pharmacy-rule .line-right { position: absolute; left: 464px; right: 0; top: 13px; height: 2px; background: var(--brand-red); }
  .pharmacy-rule .badge {
    position: absolute; left: 228px; width: 238px; height: 28px; border-radius: 14px;
    background: linear-gradient(90deg, var(--brand-blue), var(--brand-red));
    color: #fff; font-weight: 700; font-size: 18px; text-align: center; line-height: 28px;
  }

  .pharmacy-note { position: absolute; left: 0; right: 0; top: 313px; text-align: center; color: var(--ink); font-size: 16px; }
  .pharmacy-note p { line-height: 20px; }
  .pharmacy-note .admin { margin-top: 3px; }

  .wave { position: absolute; left: 0; bottom: 0; width: 742px; height: 70px; }

  .tagline {
    position: absolute; left: 0; right: 0; top: 262px; text-align: center;
    font-weight: 700; font-size: 24px; letter-spacing: -0.3px;
  }
  .tagline .red { color: var(--brand-red); }
  .tagline .blue { color: var(--brand-blue); }

  .site-note { position: absolute; left: 0; right: 0; top: 376px; text-align: center; color: #fff; font-size: 16px; }
  .site-note a { color: var(--brand-red); text-decoration: none; }
</style>
</head>
<body>

<section class="card card--front">
  <div class="wordmark">ScriptWay</div>

  <ul class="benefits">
    <li>Save up to 99%</li>
    <li>100% HIPPA Compliat</li>
    <li>Lower Price Guarentee</li>
    <li>Covers 9 Days Supply And Pets Meds</li>
  </ul>

  <dl class="processing">
    <div class="row"><dt>BIN :</dt><dd>014520</dd></div>
    <div class="row"><dt>ID :</dt><dd>SW0000</dd></div>
    <div class="row"><dt>PCN :</dt><dd>SCWY2</dd></div>
    <div class="row"><dt>GROUP :</dt><dd>SCWAY</dd></div>
    <div class="row"><dt>CONDORS :</dt><dd>36805</dd></div>
  </dl>

  <div class="pharmacy-rule">
    <span class="line-left"></span>
    <span class="badge">ATTENTION PHARMACY</span>
    <span class="line-right"></span>
  </div>

  <div class="pharmacy-note">
    <p>If you are unable to process a prescription through our program</p>
    <p>Please Call Us (800)-555-0142</p>
    <p class="admin">Administrated by Meridian Claims- This is Not Insurance</p>
  </div>

  <svg class="wave" viewBox="0 0 742 70" aria-hidden="true">
    <path d="M380 40 C520 38 650 22 742 0 L742 18 C640 34 520 44 380 40 Z" fill="var(--brand-red)"/>
    <path d="M0 38 C120 2 260 2 380 30 C520 48 650 38 742 28 L742 70 L0 70 Z" fill="var(--brand-blue)"/>
    <path d="M380 30 C520 46 650 38 742 24 L742 30 C650 42 520 50 380 30 Z" fill="#ffffff"/>
  </svg>
</section>

<section class="card card--back">
  <div class="wordmark">ScriptWay</div>
  <p class="tagline"><span class="red">PRESCRIPTION</span> <span class="blue">DISCOUNT</span> <span class="red">LEADER</span></p>
  <p class="site-note">Please visit our website <a href="#">www.scriptway.com</a> for current drug prices</p>
</section>

</body>
</html>
```